Single Sided 1 Page Tour Flyer in the same theme as previous brochure

We need a single sided 8.5 x 11 flyer in the same theme and color scheme as the previous brochure we worked on together. the flyer should include the following

1. company logo up top (just like on the front panel of previous brochure
2. tour name "Silver Meadow Trail Loop" also on the top
3. a large photo towards the top of the flyer, similar to the brochure front
4. 3 panels of text: left one for tour prices, whats included, additional notes, center and right panels for tour program details (day 1, day 2, etc)
5. below that, a few lines for additional details, like small print and stuff
6. company address, phone numbers, email address, and website link
6. below that a banner of small photos, maybe 4 in a row, similar to the brochure

details of the actual tour can be found at this link:
http://bluefernvoyage.ru/en/tours/silver-meadow-trail-loop-11-days/

once again, we would love for the flyer to be in the same theme and style as the other brochure, so it matches, we loved the previous work!!

```html
<!DOCTYPE html>
<html lang="en">
<head>
<meta charset="utf-8">
<title>Silver Meadow Trail Loop – Tour Flyer</title>
<link href="https://fonts.googleapis.com/css2?family=PT+Sans:wght@400;700&family=Open+Sans:wght@300;400;600&display=swap" rel="stylesheet">
<style>
:root{
  --red:#c8161d;
  --red-dark:#9e0f14;
  --gold:#f2b707;
  --gold-light:#ffd34a;
  --ink:#3a3a3a;
  --grey:#6d6e70;
  --grey-light:#e6e6e6;
  --charcoal:#3b3b3d;
  --paper:#ffffff;
}
*{box-sizing:border-box;margin:0;padding:0}
html,body{width:972px;height:1200px;overflow:hidden;background:#f4f4f4}
body{font-family:"PT Sans",Arial,sans-serif;color:var(--ink)}
.flyer{position:relative;width:972px;height:1200px;background:var(--paper);overflow:hidden}
.abs{position:absolute}

/* header */
.brand{left:38px;top:50px;display:flex;align-items:center;gap:12px}
.brand-dot{width:46px;height:46px;border-radius:50%;background:var(--gold)}
.brand-name{font-family:"PT Sans",Arial,sans-serif;font-weight:700;font-size:34px;color:var(--charcoal);letter-spacing:.5px}
.tour-title{right:40px;top:26px;font-family:"Open Sans",Arial,sans-serif;font-weight:400;font-size:33px;color:var(--charcoal)}
.top-art{left:0;top:0}

/* photos */
.oval{position:absolute;border-radius:50%;border:4px solid #fff;box-shadow:0 6px 10px rgba(0,0,0,.45)}
.oval-streets{left:87px;top:420px;width:183px;height:128px;background:radial-gradient(circle at 40% 40%,#8a86a8,#3c3852 75%)}
.oval-statue{left:281px;top:424px;width:179px;height:132px;background:radial-gradient(circle at 50% 35%,#9aa6b4,#3d4650 75%)}
.oval-hotel{left:479px;top:417px;width:182px;height:131px;background:radial-gradient(circle at 50% 45%,#a58a7a,#1f2750 70%)}
.oval-falls{left:672px;top:420px;width:173px;height:113px;background:radial-gradient(circle at 50% 50%,#e9eef2,#7f93a4 75%)}

/* left column */
.itinerary-pill{left:16px;top:582px;width:282px;height:46px;border:2px solid var(--grey);border-radius:23px;display:flex;align-items:center;justify-content:center;gap:16px;font-size:24px;color:var(--charcoal);background:#fff}
.star{width:20px;height:20px}
.left-col{left:18px;top:640px;width:330px;font-size:13.5px;line-height:17px;color:var(--grey)}
.left-col p{margin-bottom:8px}
.price-table{margin:8px 0 10px 20px;width:290px;background:var(--red);border:3px solid #fff;outline:2px solid var(--red);box-shadow:0 2px 4px rgba(0,0,0,.35);display:grid;grid-template-columns:repeat(3,1fr);text-align:center;color:#fff;padding:4px 0}
.price-table .label{font-weight:700;font-size:16px}
.price-table .amount{font-size:17px}
.left-col h3{font-weight:400;font-size:16px;color:var(--charcoal);margin-top:4px}
.left-col ul{list-style:none;margin-bottom:6px}
.left-col li{padding-left:10px;position:relative}
.left-col li::before{content:"";position:absolute;left:0;top:6px;width:6px;height:6px;border-radius:50%;background:var(--red)}

/* program */
.route{left:367px;top:597px;width:580px;font-size:23px;line-height:30px;font-weight:400;color:var(--red);letter-spacing:.4px}
.program{top:672px;font-size:14px;line-height:17.4px;color:var(--grey);text-align:justify}
.program-mid{left:367px;width:282px}
.program-right{left:668px;width:272px}
.program p{margin-bottom:10px}
.day{color:var(--red);font-weight:700;font-size:15px;white-space:nowrap}

/* footer */
.fine-print{left:18px;top:1078px;width:500px;font-size:10.5px;line-height:13px;color:var(--charcoal)}
.fine-print p{margin-bottom:2px}
.bottom-art{left:0;top:1030px}
.price-badge{left:552px;top:1052px;width:170px;height:114px;border-radius:50%;background:radial-gradient(ellipse at 50% 35%,#e0282e,var(--red-dark));border:3px solid #fff;box-shadow:0 3px 6px rgba(0,0,0,.4);text-align:center;color:#fff;padding-top:16px}
.price-badge .from{font-weight:700;font-size:16px;line-height:17px}
.price-badge .amount{font-weight:700;font-size:37px;line-height:42px;color:#fff3d6}
.contact{right:34px;top:1082px;text-align:right;color:#fff;font-size:15px;line-height:20px;font-style:normal}
.contact .row{display:flex;justify-content:flex-end;align-items:center;gap:6px}
.contact svg{width:13px;height:13px}
.contact .gap{margin-top:6px}
.website{left:84px;top:1174px;color:#fff;font-size:15px;display:flex;align-items:center;gap:8px}
.website .dot{width:11px;height:11px;border-radius:50%;background:var(--gold)}
</style>
</head>
<body>
<div class="flyer">

  <svg class="abs top-art" width="972" height="600" viewBox="0 0 972 600" aria-hidden="true">
    <defs>
      <linearGradient id="greySweep" x1="0" y1="0" x2="1" y2="0">
        <stop offset="0" stop-color="#ffffff"/>
        <stop offset=".6" stop-color="#e9e9e9"/>
        <stop offset="1" stop-color="#d4d4d4"/>
      </linearGradient>
      <linearGradient id="goldSweep" x1="0" y1="0" x2="1" y2="0">
        <stop offset="0" stop-color="#e9a400"/>
        <stop offset=".5" stop-color="#ffd34a"/>
        <stop offset="1" stop-color="#e9a400"/>
      </linearGradient>
    </defs>
    <path d="M0 150 C300 120 600 60 972 70 L972 175 L0 175 Z" fill="url(#greySweep)"/>
    <path d="M0 160 C320 140 640 120 972 150 L972 165 C640 138 320 156 0 172 Z" fill="url(#goldSweep)"/>
    <path d="M0 545 C340 590 640 560 972 520 L972 600 L0 600 Z" fill="#fff"/>
    <path d="M0 548 C340 592 640 562 972 522" stroke="url(#goldSweep)" stroke-width="9" fill="none"/>
  </svg>

  <div class="abs hero" role="img" aria-label="Night view of a lit suspension bridge over a bay with city lights beyond"
       style="left:0;top:166px;width:972px;height:388px;clip-path:path('M0 6 C320 -18 640 -34 972 -10 L972 356 C640 396 340 428 0 380 Z');background:linear-gradient(180deg,#5d5a8c 0%,#7d76a8 35%,#a08fb4 55%,#3a3f66 70%,#2b2c44 85%,#c47a3a 100%)"></div>

  <div class="abs brand">
    <span class="brand-dot"></span>
    <span class="brand-name">Blue Fern Voyage</span>
  </div>
  <h1 class="abs tour-title">Silver Meadow Trail Loop</h1>

  <div class="oval oval-streets" role="img" aria-label="Street name signs on a city corner"></div>
  <div class="oval oval-statue" role="img" aria-label="Crowned statue against the sky"></div>
  <div class="oval oval-hotel" role="img" aria-label="Illuminated hotel building at dusk"></div>
  <div class="oval oval-falls" role="img" aria-label="Waterfall with a tour boat in the mist"></div>

  <div class="abs itinerary-pill">
    <svg class="star" viewBox="0 0 20 20" aria-hidden="true"><circle cx="10" cy="10" r="8" fill="var(--gold)"/></svg>
    <span>Tour Itinerary</span>
    <svg class="star" viewBox="0 0 20 20" aria-hidden="true"><circle cx="10" cy="10" r="8" fill="var(--gold)"/></svg>
  </div>

  <section class="abs left-col">
    <p style="margin-bottom:0">The cost of tour for one person<br>(Personalize in process of purchasing)</p>
    <div class="price-table">
      <span class="label">DBL</span><span class="label">SNGL</span><span class="label">TRPL</span>
      <span class="amount">$1,495</span><span class="amount">$1,995</span><span class="amount">$1,395</span>
    </div>
    <h3>Included in Price:</h3>
    <ul>
      <li>Double occupancy in hotels along the route</li>
      <li>Breakfasts</li>
      <li>Excursions as per itinerary</li>
    </ul>
    <h3>Not Included in Price:</h3>
    <ul>
      <li>Domestic airfare</li>
      <li>Tips for the driver and guide</li>
    </ul>
    <p>*Departure from Buffalo Airport (BUF) is also possible (transfer is not included in the program, and is an additional charge)</p>
    <p>Participants can also return to New York, Manhattan, or JFK Airport (transfer is free). Departure from JFK airport is not possible on the 11th Day due to time constraints.</p>
    <p>*We recommend extending your trip with additional nights in New York, for leisure time in Manhattan, Broadway shows, shopping, and much more.</p>
  </section>

  <h2 class="abs route">New York, Washington, D.C., Philadelphia, Boston, Montreal, Quebec, Ottawa, Niagara Falls</h2>

  <section class="abs program program-mid">
    <p><span class="day">Day 1</span> Arrival to Washington, D.C., registration in hotel. Overnight in Washington, D.C.</p>
    <p><span class="day">Day 2</span> Sightseeing tour of Washington, D.C.: memorials, Capitol Building, White House, museums, and much more. Overnight in Washington, D.C.</p>
    <p><span class="day">Day 3</span> Departure to Philadelphia. Sightseeing tour of Philadelphia. Departure to New York, leisure time in the evening. Overnight in New York</p>
    <p><span class="day">Day 4</span> Sightseeing tour of New York: Manhattan, Wall Street, United Nations Building, Broadway, Times Square. *optional cruise to the Statue of Liberty and Ellis Island. Overnight in New York</p>
    <p><span class="day">Day 5</span> Departure to Boston. Sightseeing tour of Boston, Harvard University. Overnight in Boston</p>
  </section>

  <section class="abs program program-right">
    <p><span class="day">Day 6</span> Departure to Montreal, sightseeing tour of the city. Overnight in Montreal</p>
    <p><span class="day">Day 7</span> Sightseeing tour of Quebec, return to Montreal. Overnight in Montreal</p>
    <p><span class="day">Day 8</span> Second part of sightseeing tour of Montreal. Old Town, Montreal Port, Notre Dame de Montreal. Departure to Ottawa, sightseeing tour of Ottawa. Overnight in Ottawa</p>
    <p><span class="day">Day 9</span> Departure to Rockport, cruise of 1,000 Islands, Departure to Toronto. Overnight in Toronto</p>
    <p><span class="day">Day 10</span> Sightseeing tour of Toronto. Departure to Niagara Falls. Cruise to the Niagara Falls. Overnight in Niagara Falls</p>
    <p><span class="day">Day 11</span> Transfer to Toronto Airport (YYZ). End of tour program</p>
  </section>

  <svg class="abs bottom-art" width="972" height="170" viewBox="0 0 972 170" aria-hidden="true">
    <defs>
      <linearGradient id="darkBand" x1="0" y1="0" x2="0" y2="1">
        <stop offset="0" stop-color="#4a4a4c"/>
        <stop offset="1" stop-color="#2c2c2e"/>
      </linearGradient>
    </defs>
    <path d="M600 40 C760 10 880 0 972 8" stroke="#cfcfcf" stroke-width="3" fill="none"/>
    <path d="M640 170 C700 90 800 40 972 22 L972 170 Z" fill="url(#darkBand)"/>
    <path d="M0 136 L600 136 C640 136 660 150 680 170 L0 170 Z" fill="var(--red)"/>
  </svg>

  <section class="abs fine-print">
    <p>**order of sights of interest may change with advance notice</p>
    <p>* Blue Fern Voyage, Inc. cannot be held liable for complications arising from improperly filled out forms, passports or visas, especially upon crossing international borders.</p>
    <p>* Blue Fern Voyage, Inc. cannot be held liable for forgotten personal belongings left in hotels, aboard the bus, or lost throughout the duration of the tour.</p>
  </section>

  <div class="abs price-badge">
    <div class="from">Cost for<br>1 person from</div>
    <div class="amount">$1,495</div>
  </div>

  <address class="abs contact">
    <div class="row"><svg viewBox="0 0 12 12" aria-hidden="true"><path d="M6 0a4 4 0 0 0-4 4c0 3 4 8 4 8s4-5 4-8a4 4 0 0 0-4-4zm0 5.5A1.5 1.5 0 1 1 6 2.5a1.5 1.5 0 0 1 0 3z" fill="var(--gold)"/></svg>4150 Larkspur Avenue</div>
    <div>Suite #310</div>
    <div>Fairview, CA 90512</div>
    <div class="row gap"><svg viewBox="0 0 12 12" aria-hidden="true"><path d="M2.5 0.8l2 2-1 1.4c.6 1.5 1.8 2.7 3.3 3.3l1.4-1 2 2-1.2 1.9C5 9.8 1.9 6.7 0.6 2z" fill="var(--gold)"/></svg>+1 (800) 555-0142</div>
    <div class="row"><svg viewBox="0 0 12 12" aria-hidden="true"><rect x="0.5" y="2" width="11" height="8" fill="var(--gold)"/><path d="M0.5 2l5.5 4.5 5.5-4.5" stroke="#333" stroke-width="1" fill="none"/></svg>info@bluefernvoyage.com</div>
  </address>

  <div class="abs website"><span class="dot"></span>www.bluefernvoyage.com</div>

</div>
</body>
</html>
```